Criação de Peça Gráfica (unidade) para Segurança & Vigilância
A empresa queria:
" Fornecemos, alugamos, instalamos e damos manutenção, bem como, fornecemos mão de obra alocada residente para que o nosso cliente tenha total conforto e segurança. "

```html
<!DOCTYPE html>
<html lang="pt-BR">
<head>
<meta charset="UTF-8">
<title>Vantel Sistema de Segurança — Folder</title>
<link rel="stylesheet" href="https://fonts.googleapis.com/css2?family=Exo+2:ital,wght@0,700;1,800&family=Open+Sans:wght@400;600&display=swap">
<style>
  :root {
    --bg: #e6e9ec;
    --paper: #ffffff;
    --blue: #1f88d0;
    --blue-deep: #1666a6;
    --ink: #111418;
    --night: #0b1622;
    --text: #5d6670;
    --heading: #1f88d0;
  }
  * { box-sizing: border-box; margin: 0; padding: 0; }
  html, body { width: 1200px; height: 1200px; overflow: hidden; }
  body {
    background: var(--bg);
    font-family: "Open Sans", Arial, sans-serif;
    position: relative;
  }
  .panel {
    position: absolute;
    top: 290px;
    width: 260px;
    height: 620px;
    background: var(--paper);
    overflow: hidden;
    box-shadow: 0 10px 30px rgba(0,0,0,.12);
  }
  .panel--about  { left: 70px; }
  .panel--middle { left: 330px; }
  .panel--right  { left: 590px; }
  .panel--cover  { left: 890px; background: var(--night); }

  .shapes { position: absolute; inset: 0; width: 100%; height: 100%; }

  .brand { position: absolute; z-index: 2; }
  .brand__name {
    font-family: "Exo 2", Arial, sans-serif;
    font-weight: 700;
    font-size: 30px;
    line-height: 1;
    letter-spacing: 1px;
    color: #fff;
  }
  .brand__tag {
    font-family: "Open Sans", Arial, sans-serif;
    font-size: 6.5px;
    letter-spacing: 1.6px;
    text-transform: uppercase;
    color: #fff;
    margin-top: 3px;
  }
  .brand--dark .brand__name, .brand--dark .brand__tag { color: var(--ink); }

  .copy { position: absolute; left: 22px; right: 22px; z-index: 2; }
  .copy h2 {
    font-family: "Exo 2", Arial, sans-serif;
    font-weight: 700;
    font-size: 13px;
    color: var(--heading);
    margin-bottom: 8px;
  }
  .copy p {
    font-size: 8.5px;
    line-height: 1.55;
    color: var(--text);
    margin-bottom: 9px;
  }

  .art { position: absolute; z-index: 1; }
  .art--icons {
    left: 22px; right: 22px; top: 430px; height: 80px;
    background: radial-gradient(circle at 50% 50%, #d6ebf8 0%, #eef6fc 60%, #ffffff 100%);
    border-radius: 4px;
  }
  .art--camera {
    left: -260px; width: 520px; top: 0; height: 270px;
    background: linear-gradient(115deg, #6e8f5a 0%, #a7b99a 30%, #e7ece9 50%, #c9cfd4 62%, #7d9a6a 85%, #5d7d4c 100%);
  }
  .panel--right .art--camera { left: -260px; }
  .panel--middle .art--camera { left: 0; }
  .art--hand {
    left: 0; right: 0; top: 90px; height: 390px;
    background: radial-gradient(circle at 60% 45%, #3c6f99 0%, #1b3b5a 35%, #0c1a29 75%);
  }

  .headline {
    position: absolute;
    z-index: 3;
    left: 22px;
    top: 395px;
    font-family: "Exo 2", Arial, sans-serif;
    font-weight: 800;
    font-style: italic;
    font-size: 22px;
    line-height: 1.08;
    text-transform: uppercase;
    color: #fff;
    letter-spacing: .5px;
  }
</style>
</head>
<body>

  <!-- Inside left panel -->
  <section class="panel panel--about">
    <svg class="shapes" viewBox="0 0 260 620" aria-hidden="true">
      <polygon points="0,0 260,0 260,30 150,105 0,105" fill="#111418"/>
      <polygon points="150,105 260,30 260,58 190,105" fill="#1f88d0"/>
      <polygon points="0,620 0,560 140,620" fill="#1f88d0"/>
      <polygon points="60,620 260,545 260,620" fill="#111418"/>
      <polygon points="170,586 260,552 260,575 228,590" fill="#1f88d0"/>
    </svg>
    <div class="brand" style="left:22px; top:40px;">
      <div class="brand__name">vantel</div>
      <div class="brand__tag">Sistema de Segurança</div>
    </div>
    <div class="copy" style="top:130px;">
      <h2>Sobre Vantel</h2>
      <p>Somos especialistas em segurança eletrônica, com soluções completas para empresas e residências em toda a região.</p>
      <p>Fornecemos, alugamos, instalamos e damos manutenção em sistemas de monitoramento.</p>
      <p>Equipe técnica qualificada para atender cada projeto.</p>
    </div>
    <div class="art art--icons" role="img" aria-label="Rede de ícones de tecnologia e segurança conectados"></div>
  </section>

  <!-- Inside middle panel -->
  <section class="panel panel--middle">
    <div class="art art--camera" role="img" aria-label="Câmera de vigilância instalada diante de uma casa com jardim"></div>
    <svg class="shapes" viewBox="0 0 260 620" aria-hidden="true" style="z-index:1">
      <polygon points="0,0 95,0 0,70" fill="#111418"/>
      <polygon points="0,270 260,230 260,270" fill="#ffffff"/>
      <polygon points="0,250 150,270 0,290" fill="#1f88d0"/>
      <polygon points="0,620 0,570 110,620" fill="#111418"/>
      <polygon points="120,620 260,560 260,620" fill="#1f88d0"/>
    </svg>
    <div class="copy" style="top:305px;">
      <h2>Sobre Vantel</h2>
      <p>Oferecemos mão de obra alocada residente para que nosso cliente tenha total conforto e segurança.</p>
      <p>Câmeras, alarmes e controle de acesso integrados em uma só plataforma.</p>
    </div>
  </section>

  <!-- Inside right panel -->
  <section class="panel panel--right">
    <div class="art art--camera" role="img" aria-label="Continuação da foto da câmera de vigilância"></div>
    <svg class="shapes" viewBox="0 0 260 620" aria-hidden="true" style="z-index:1">
      <polygon points="0,270 0,230 260,190 260,270" fill="#ffffff"/>
      <polygon points="160,270 260,215 260,270" fill="#1f88d0"/>
      <polygon points="0,620 0,575 150,620" fill="#1f88d0"/>
      <polygon points="90,620 260,550 260,620" fill="#111418"/>
    </svg>
    <div class="brand brand--dark" style="right:22px; top:28px; text-align:right;">
      <div class="brand__name">vantel</div>
      <div class="brand__tag">Sistema de Segurança</div>
    </div>
    <div class="copy" style="top:305px;">
      <p>Atendimento rápido e suporte técnico em todas as etapas da instalação.</p>
      <p>Projetos sob medida com equipamentos de alta qualidade e garantia.</p>
      <p>Solicite uma visita técnica sem compromisso.</p>
    </div>
  </section>

  <!-- Front cover -->
  <section class="panel panel--cover">
    <div class="art art--hand" role="img" aria-label="Mão tocando ícones digitais de tecnologia"></div>
    <svg class="shapes" viewBox="0 0 260 620" aria-hidden="true" style="z-index:2">
      <polygon points="0,0 260,0 260,90 0,90" fill="#111418"/>
      <polygon points="215,90 260,70 260,250 240,250" fill="#1f88d0"/>
      <polygon points="0,620 0,520 260,580 260,620" fill="#ffffff"/>
      <polygon points="0,520 130,550 0,575" fill="#1f88d0"/>
      <polygon points="130,620 260,560 260,620" fill="#111418"/>
      <polygon points="190,600 260,575 260,590" fill="#1f88d0"/>
    </svg>
    <div class="brand" style="left:0; right:0; top:28px; text-align:center;">
      <div class="brand__name">vantel</div>
      <div class="brand__tag">Sistema de Segurança</div>
    </div>
    <h1 class="headline">Integrando<br>Tecnologia<br>e Segurança</h1>
  </section>

</body>
</html>
```